Personal Injury Book Ad Photo Set

I need a series of images for a Pagebloom ad campaign for promoting a book titled "A Plain Guide to Your Injury Recovery Case".

```html
<!DOCTYPE html>
<html lang="en">
<head>
<meta charset="utf-8">
<title>Making Sense of an Accident Claim – Ad 2:3</title>
<link rel="stylesheet" href="https://fonts.googleapis.com/css2?family=Poppins:wght@300;700&family=Montserrat:wght@700&family=Tinos&family=Allura&display=swap">
<style>
  :root {
    --stage-dark: #444244;
    --stage-light: #b8b8b8;
    --ink: #222427;
    --accent: #e08a0c;
    --card-top: #ffffff;
    --card-bottom: #e3eaf2;
    --label: #ffffff;
  }
  * { margin: 0; padding: 0; box-sizing: border-box; }
  html, body { width: 1200px; height: 1200px; overflow: hidden; }
  body {
    position: relative;
    background: linear-gradient(135deg, var(--stage-dark) 0%, #7a797a 45%, var(--stage-light) 100%);
    font-family: "Poppins", sans-serif;
  }
  .ad-card {
    position: absolute;
    left: 322px; top: 161px;
    width: 557px; height: 836px;
    background: linear-gradient(160deg, var(--card-top) 35%, var(--card-bottom) 100%);
    color: var(--ink);
  }
  .title-line {
    position: absolute;
    left: 0; width: 100%;
    text-align: center;
    line-height: 1;
    white-space: nowrap;
  }
  .title-line .connector {
    font-family: "Tinos", "Times New Roman", serif;
    font-weight: 400;
    letter-spacing: -1px;
    margin-right: 4px;
  }
  .title-line .keyword {
    font-family: "Poppins", sans-serif;
    font-weight: 700;
  }
  .title-line .keyword.accent { color: var(--accent); }
  .title-first { top: 40px; }
  .title-first .connector { font-size: 44px; }
  .title-first .keyword { font-size: 66px; }
  .title-second { top: 110px; }
  .title-second .connector { font-size: 44px; }
  .title-second .keyword { font-size: 66px; }
  .title-third { top: 178px; }
  .title-third .keyword { font-size: 66px; }

  .book-mockup {
    position: absolute;
    left: 172px; top: 270px;
    width: 205px; height: 320px;
    background: linear-gradient(170deg, #f3f7fb 0%, #c9d6e4 60%, #b7c8db 100%);
    box-shadow: 6px 8px 14px rgba(0,0,0,0.18);
  }

  .subtitle-line {
    position: absolute;
    left: 0; width: 100%;
    text-align: center;
    font-weight: 300;
    font-size: 29px;
    line-height: 1;
    letter-spacing: 0.38em;
    padding-left: 0.38em;
    white-space: nowrap;
  }
  .subtitle-line .highlight { color: var(--accent); }
  .subtitle-1 { top: 627px; }
  .subtitle-2 { top: 668px; }
  .subtitle-3 { top: 707px; }

  .author-signature {
    position: absolute;
    left: 0; width: 100%; top: 760px;
    text-align: center;
    font-family: "Allura", cursive;
    font-size: 44px;
    line-height: 1;
  }

  .format-label {
    position: absolute;
    left: 0; width: 100%; top: 1055px;
    text-align: center;
    font-family: "Montserrat", sans-serif;
    font-weight: 700;
    font-size: 52px;
    line-height: 1;
    color: var(--label);
  }
</style>
</head>
<body>
  <section class="ad-card">
    <h1 class="book-title">
      <span class="title-line title-first"><span class="connector">Making</span><span class="keyword">SENSE</span></span>
      <span class="title-line title-second"><span class="connector">of an</span><span class="keyword accent">ACCIDENT</span></span>
      <span class="title-line title-third"><span class="keyword accent">CLAIM</span></span>
    </h1>

    <div class="book-mockup" role="img" aria-label="Hardcover book showing the cover with a judge's gavel and stethoscope"></div>

    <p class="subtitle">
      <span class="subtitle-line subtitle-1">A PLAIN GUIDE</span>
      <span class="subtitle-line subtitle-2">TO YOUR <span class="highlight">INJURY</span></span>
      <span class="subtitle-line subtitle-3"><span class="highlight">RECOVERY</span> CASE</span>
    </p>

    <p class="author-signature">Author Name</p>
  </section>

  <p class="format-label">AD RATIO 2:3</p>
</body>
</html>
```